I would like to update my one-page service sheet to provide a more professional/polished look and...

One page service sheet - with content on both the front and back. I've uploaded my current one page service sheet to provide background. I've also included a service sheet that I recently received from another business owner (from a very different business) that is a representation of the kind of feel I'm looking for. My business website may be found at: www.torvilunconsulting.com

```html
<!DOCTYPE html>
<html lang="en">
<head>
<meta charset="utf-8">
<title>Torvilun Consulting – Service Sheet</title>
<link rel="stylesheet" href="https://fonts.googleapis.com/css2?family=Montserrat:ital,wght@0,400;0,600;0,700;0,800;1,700&display=swap">
<style>
  :root {
    --backdrop: #e0e0e0;
    --paper: #fbfbfb;
    --orange: #ee6c16;
    --slate: #3a4656;
    --slate-text: #2f3a48;
    --white: #ffffff;
    --sky-deep: #3c4f86;
    --sky-warm: #b9788c;
  }
  * { box-sizing: border-box; margin: 0; padding: 0; }
  html, body { width: 1200px; height: 850px; overflow: hidden; }
  body {
    background: var(--backdrop);
    font-family: "Montserrat", Arial, sans-serif;
    position: relative;
  }
  .sheet {
    position: absolute;
    top: 35px;
    width: 552px;
    height: 780px;
    background: var(--paper);
    overflow: hidden;
    box-shadow: 0 4px 14px rgba(0,0,0,0.12);
  }
  .sheet--front { left: 36px; }
  .sheet--back { left: 612px; }
  .block { position: absolute; }

  .photo { position: absolute; }
  .photo--climbers {
    left: 0; top: 0; width: 330px; height: 270px;
    background: linear-gradient(160deg, #2a3a6e 0%, var(--sky-deep) 40%, var(--sky-warm) 80%, #4a3a34 100%);
  }
  .photo--binoculars {
    left: 290px; top: 386px; width: 262px; height: 226px;
    background: radial-gradient(circle at 45% 40%, #6a8aa0 0%, #2d3238 35%, #cfc7c0 75%, #e9e4df 100%);
  }
  .photo--rowing {
    left: 290px; top: 130px; width: 262px; height: 210px;
    background: linear-gradient(200deg, #f2f4f6 0%, #b9c6d2 45%, #27426e 70%, #dfe6ea 100%);
  }
  .photo--tablet {
    left: 0; top: 400px; width: 280px; height: 240px;
    background: radial-gradient(circle at 50% 45%, #3fa7f0 0%, #174a8c 35%, #0b1a33 80%);
  }
  .accent-wedge { position: absolute; left: 230px; top: 170px; }

  .brand {
    position: absolute; right: 30px; top: 100px;
    display: flex; align-items: center; gap: 8px;
    font-weight: 800; font-size: 17px; letter-spacing: 1.5px;
    color: var(--slate-text);
  }
  .brand__mark { width: 12px; height: 12px; background: var(--orange); }

  .headline-box {
    left: 290px; top: 170px; width: 262px; height: 150px;
    background: var(--orange);
    padding: 24px 20px;
  }
  .headline {
    color: var(--white); font-weight: 800; font-size: 22px; line-height: 1.2;
  }

  .section-title {
    font-weight: 800; font-size: 14px; color: var(--slate-text);
    text-transform: uppercase; letter-spacing: 0.3px;
  }
  .section-sub {
    margin-top: 4px;
    font-weight: 700; font-style: italic; font-size: 12px;
    color: var(--orange); line-height: 1.3;
  }

  .service-panel {
    background: var(--slate);
    color: var(--white);
    padding: 22px 22px;
    font-size: 8.5px; line-height: 1.45;
  }
  .service-panel li { list-style: none; margin-bottom: 7px; }
  .service-panel strong { font-weight: 700; }

  .office-box {
    background: var(--orange); color: var(--white);
    padding: 18px 24px; font-size: 8.5px; line-height: 1.4;
  }
  .office-box h4 { font-weight: 800; font-size: 13px; letter-spacing: 0.3px; }
  .office-box p { margin-bottom: 8px; }

  .phone {
    display: flex; align-items: center; gap: 8px;
    font-weight: 700; font-size: 16px; color: var(--slate-text);
  }
  .contact-band {
    background: var(--slate); color: var(--white);
    font-size: 9px; line-height: 1.6;
    padding: 34px 20px 0;
  }
</style>
</head>
<body>

<section class="sheet sheet--front">
  <div class="photo photo--climbers" role="img" aria-label="Photo of two climbers helping each other up a rock face at dusk"></div>
  <svg class="accent-wedge" width="70" height="120" viewBox="0 0 70 120" aria-hidden="true">
    <polygon points="60,0 70,0 70,100 0,120" fill="#2f4a8a"/>
  </svg>

  <div class="brand"><span class="brand__mark"></span>TORVILUN CONSULTING</div>

  <div class="block headline-box">
    <p class="headline">Replace confusion and hesitation with clarity and resolve</p>
  </div>

  <div class="block" style="left:24px; top:332px; width:510px;">
    <h2 class="section-title">Growth Strategy &amp; Innovation</h2>
    <p class="section-sub">Discover what's needed to reach the next stage of growth.</p>
  </div>

  <div class="block service-panel" style="left:0; top:386px; width:290px; height:200px;">
    <ul>
      <li><strong>Growth Strategy &amp; Business Model Review.</strong> Gain an objective perspective on your growth strategy and focus areas.</li>
      <li><strong>Revenue Acceleration &amp; Lead Generation.</strong> Define and execute strategies and tactics to drive demand and the pipeline.</li>
      <li><strong>Execution and Scale.</strong> Enable your people, processes and technology for the demands of growth.</li>
      <li><strong>Pricing Strategies.</strong> Strategically price products and services.</li>
      <li><strong>Growth Training.</strong> Group and individual training/coaching.</li>
    </ul>
  </div>

  <div class="photo photo--binoculars" role="img" aria-label="Photo of hands holding binoculars with a sunset reflected in the lens"></div>

  <div class="block office-box" style="left:0; top:612px; width:300px; height:118px;">
    <h4>MINNEAPOLIS</h4>
    <p>2210 Harbor Ln, Ste 12, Edina, MN 55400</p>
    <h4>ST. PAUL</h4>
    <p>318 Alder Ct, Ste 9, Woodbury, MN 55100</p>
  </div>

  <div class="block phone" style="left:318px; top:646px;">
    <svg width="12" height="14" viewBox="0 0 12 14" aria-hidden="true"><path d="M2 1 L5 1 L6 4 L4 5 Q5 8 8 10 L9 8 L12 9 L12 12 Q8 14 4 10 Q0 6 2 1 Z" fill="#ee6c16"/></svg>
    651-555-0148
  </div>

  <div class="block contact-band" style="left:300px; top:686px; width:252px; height:94px;">
    <p>hello@torvilunconsulting.com</p>
    <p>www.torvilunconsulting.com</p>
  </div>
</section>

<section class="sheet sheet--back">
  <div class="block" style="left:30px; top:36px; width:500px;">
    <h2 class="section-title">Growth Process &amp; Execution</h2>
    <p class="section-sub">Fine-tune and formalize growth processes for efficiency, effectiveness, and scale.</p>
  </div>

  <div class="block service-panel" style="left:0; top:120px; width:300px; height:200px;">
    <ul>
      <li><strong>Innovation Capture &amp; Elaboration.</strong> Standardize idea capture, analysis, funding, rollout and innovation metrics.</li>
      <li><strong>Growth Channel Optimization.</strong> Enhance the direct and partner experience by blending digital and traditional.</li>
      <li><strong>Business Development.</strong> Formalize business development into a proactive, repeatable and measurable discipline.</li>
      <li><strong>Prospect &amp; Client Experience Mapping.</strong> Create greater client loyalty and experience, and be easier to do business with.</li>
    </ul>
  </div>

  <div class="photo photo--rowing" role="img" aria-label="Photo of a rowing crew pulling oars together on the water"></div>

  <div class="block" style="left:30px; top:346px; width:500px;">
    <h2 class="section-title">Growth Solutions &amp; Analytics</h2>
    <p class="section-sub">Get the right capabilities in place to support your growth journey.</p>
  </div>

  <div class="photo photo--tablet" role="img" aria-label="Photo of hands holding a tablet with glowing business icons above it"></div>

  <div class="block service-panel" style="left:280px; top:410px; width:272px; height:230px;">
    <ul>
      <li><strong>Technology Strategy &amp; Roadmap.</strong> Ensure that the right technology is in place for each step of your growth journey.</li>
      <li><strong>Software Selection.</strong> Identify the specific capabilities and vendors that are most appropriate for your business.</li>
      <li><strong>Project Leadership.</strong> Get critical projects over the finish line.</li>
      <li><strong>Disruptive Trends.</strong> Demystify Digital, Big Data, Artificial Intelligence and Internet of Things to create advantage.</li>
      <li><strong>Critical Metrics.</strong> Determine the leading and lagging metrics that are most critical for your business.</li>
    </ul>
  </div>

  <div class="block office-box" style="left:0; top:620px; width:300px; height:110px;">
    <h4>MINNEAPOLIS</h4>
    <p>2210 Harbor Ln, Ste 12, Edina, MN 55400</p>
    <h4>ST. PAUL</h4>
    <p>318 Alder Ct, Ste 9, Woodbury, MN 55100</p>
  </div>

  <div class="block phone" style="left:318px; top:656px;">
    <svg width="12" height="14" viewBox="0 0 12 14" aria-hidden="true"><path d="M2 1 L5 1 L6 4 L4 5 Q5 8 8 10 L9 8 L12 9 L12 12 Q8 14 4 10 Q0 6 2 1 Z" fill="#ee6c16"/></svg>
    651-555-0148
  </div>

  <div class="block contact-band" style="left:300px; top:690px; width:252px; height:90px;">
    <p>hello@torvilunconsulting.com</p>
    <p>www.torvilunconsulting.com</p>
  </div>
</section>

</body>
</html>
```